Pipeline management & construction company needs nice brochure

Red Mesa Engineering & Construction, LLC (www.redmesaec.example) is a company focused on the midstream oil and gas / pipeline business. We plan, route, design, manage, and construction pipelines and related facilities. We need a brochure to summarize our services as well as give a brief listing of projects completed/desired.

Industry/Entity Type

Construction

Font styles to use
Serif

```html
<!DOCTYPE html>
<html lang="en">
<head>
<meta charset="utf-8">
<title>RMEC Approach – Brochure Page</title>
<link href="https://fonts.googleapis.com/css2?family=PT+Serif:ital,wght@0,400;0,700;1,400&family=Lato:wght@400;700&display=swap" rel="stylesheet">
<style>
  :root{
    --backdrop:#dcdcdc;
    --paper:#fbfbfb;
    --slate:#6a6a6a;
    --slate-dark:#595959;
    --gold:#e2b93b;
    --ink:#2b2b2b;
    --muted:#6f6f6f;
    --on-slate:#f4f4f4;
  }
  *{box-sizing:border-box;margin:0;padding:0}
  html,body{width:1200px;height:927px;overflow:hidden;background:var(--backdrop)}
  .page{
    position:absolute;left:270px;top:36px;width:660px;height:855px;
    background:var(--paper);box-shadow:0 6px 24px rgba(0,0,0,.15);overflow:hidden;
  }
  .page-shapes{position:absolute;inset:0;width:660px;height:855px}
  .brand{
    position:absolute;display:flex;align-items:center;gap:8px;
    font-family:"PT Serif",serif;font-weight:700;color:var(--ink);
  }
  .brand-dot{display:block;border-radius:50%;background:var(--gold)}
  .brand--header{left:34px;top:26px;font-size:14px}
  .brand--header .brand-dot{width:22px;height:22px}
  .brand--footer{left:96px;top:700px;font-size:17px}
  .brand--footer .brand-dot{width:30px;height:30px}
  .section-title{
    position:absolute;left:72px;top:102px;
    font-family:"PT Serif",serif;font-weight:400;font-size:31px;color:var(--gold);
  }
  .approach-copy{
    position:absolute;left:72px;top:160px;width:520px;
    column-count:2;column-gap:26px;
    font-family:"PT Serif",serif;font-size:11.6px;line-height:1.5;color:var(--on-slate);
    text-align:justify;hyphens:auto;
  }
  .approach-copy p{margin-bottom:15px}
  .approach-copy em{font-style:italic}
  .contact{
    position:absolute;left:96px;top:748px;
    font-family:"Lato",sans-serif;font-size:14px;line-height:1.45;color:var(--muted);
  }
  .contact-row{display:flex;align-items:flex-start;gap:6px}
  .contact-row svg{margin-top:3px;flex:none}
  .contact-indent{padding-left:18px}
  .website{
    position:absolute;right:52px;top:722px;
    font-family:"Lato",sans-serif;font-weight:700;font-size:15px;color:var(--gold);
  }
</style>
</head>
<body>
  <main class="page">
    <svg class="page-shapes" viewBox="0 0 660 855" aria-hidden="true">
      <path d="M0 84 C 200 62, 430 44, 660 72 L660 548 C 430 570, 230 648, 0 618 Z" fill="var(--slate)"/>
      <path d="M0 618 C 230 648, 430 570, 660 548 L660 560 C 430 584, 230 662, 0 632 Z" fill="var(--gold)"/>
      <rect x="26" y="352" width="30" height="272" fill="var(--gold)"/>
      <rect x="612" y="300" width="48" height="250" fill="var(--gold)"/>
    </svg>

    <div class="brand brand--header"><span class="brand-dot"></span>Red Mesa Engineering &amp; Construction, LLC</div>

    <h1 class="section-title">RMEC Approach</h1>

    <div class="approach-copy">
      <p>Our services include project management, design, construction management, and Lump Sum-Turn Key/EPC projects. By offering all of these services under one banner we feel we can react quickly to the needs of our customers, which is a must in the current market with so many private equity firms and large companies chasing the new hot beds of activity, Shale Plays.</p>
      <p>Our approach to these types of projects will be different than many of our industry peers. We intend to plan the work with the construction in mind. It sounds cliché but “plan your work and work your plan” is appropriate when it comes to pipeline and facilities projects. <em>Red Mesa Engineering &amp; Construction, LLC (RMEC)</em> is of the belief that every minute of proper planning can save valuable time and capital dollars. One too many HDDs, a fitting in the wrong location, or forgetting to consider elevation changes when planning a hydrotest can greatly impact the outcome of a project.</p>
      <p>With our team of construction focused professionals we plan to direct the design efforts toward streamlining the field construction. Construction is typically the largest portion of most AFE budgets, but sadly it is usually an afterthought, with little attention given to constructability, contract language and unit pricing methodology, or how to select the ideal construction contractor for the type of project being designed. With that in mind, we feel that if the proper attention is given to that area early on in the planning process, then we can save our customers unnecessary headaches and wasted dollars once construction is underway.</p>
    </div>

    <div class="brand brand--footer"><span class="brand-dot"></span>Red Mesa Engineering &amp; Construction, LLC</div>

    <address class="contact" style="font-style:normal">
      <div class="contact-row">
        <svg width="12" height="12" viewBox="0 0 12 12" aria-hidden="true"><path d="M6 1 L11 5.5 H9.5 V11 H7 V8 H5 V11 H2.5 V5.5 H1 Z" fill="var(--gold)"/></svg>
        <span>1450 Mesa Ridge Rd</span>
      </div>
      <div class="contact-indent">Alvarado, TX 76009</div>
      <div class="contact-row">
        <svg width="12" height="12" viewBox="0 0 12 12" aria-hidden="true"><path d="M2.5 1 L4.5 1 L5.5 3.8 L4.2 4.8 C4.9 6.4 5.8 7.3 7.3 8 L8.3 6.7 L11 7.7 L11 9.6 C11 10.4 10.3 11 9.5 11 C5 10.6 1.4 7 1 2.5 C1 1.7 1.7 1 2.5 1 Z" fill="var(--gold)"/></svg>
        <span>555 014 2290</span>
      </div>
    </address>

    <div class="website">www.redmesaec.example</div>
  </main>
</body>
</html>
```